Korvane Plumbing Business cards

Company is Korvane Plumbing.
name Dorian Malvessey, I am a plumber, drainer, gasfitter and roofer
Mobile: 0461 590 314
Email address: info@korvaneplumbing.example (check out my website for some ideas)
Website: www.korvaneplumbing.example
ABN: 42 198 603 771
LIC: 516042D

I am reliable all round plumber. I am a 24 hour emergency service. Korvane Plumbing is a professional plumbing service in the Illawarra, South Coast, Southern Sydney and Southern Highland regions of NSW. We offer a 24 hour emergency service for piece of mind to our customers. Call us now to see how we can help you. Korvane Plumbing approaches every job with attention to detail and excellent customer service. With our superior workmanship you can be confident that the job will be done right the first time around. You can rest assured with results that are guaranteed to last.

Target Market(s)

the general public

Contact Information for Business Card

look up website for some ideas something with similar colours to logo and new modern and to catch the eye.

Colors
fdfdfd
ffffff
000000
7f7f7f
aaaaaa
33a6d7
0492cd

Requirements
Must have
• all contact details
• company- Korvane Plumbing
• name- Dorian Malvessey
• number mobile- 0461 590 314
• Email address- info@korvaneplumbing.example
• Website- www.korvaneplumbing.example
• ABN- 42 198 603 771
• LIC- 516042D

```html
<!DOCTYPE html>
<html lang="en">
<head>
<meta charset="utf-8">
<title>Korvane Plumbing – Business Cards</title>
<link rel="stylesheet" href="https://fonts.googleapis.com/css2?family=Montserrat:wght@400;500;600;700&display=swap">
<style>
  :root {
    --paper: #fdfdfd;
    --white: #ffffff;
    --black: #000000;
    --grey-dark: #7f7f7f;
    --grey-light: #aaaaaa;
    --blue: #33a6d7;
    --blue-deep: #0492cd;
    --stage: #e9e9e9;
  }
  * { box-sizing: border-box; margin: 0; padding: 0; }
  html, body {
    width: 1200px; height: 780px; overflow: hidden;
    background: var(--stage);
    font-family: "Montserrat", sans-serif;
  }
  .stage { position: relative; width: 1200px; height: 780px; }

  .card {
    position: absolute;
    border-radius: 22px;
    overflow: hidden;
    box-shadow: 0 10px 28px rgba(0,0,0,.18);
  }

  /* Front card */
  .card-front {
    left: 110px; top: 90px; width: 380px; height: 600px;
    background: var(--black);
  }
  .front-top {
    position: absolute; left: 0; top: 0; width: 100%; height: 300px;
    background: linear-gradient(180deg, var(--white), var(--paper) 70%, #ececec);
  }
  .front-swoosh { position: absolute; left: 0; top: 230px; width: 380px; height: 120px; }
  .brand {
    position: absolute; left: 0; right: 0; top: 105px;
    display: flex; align-items: center; justify-content: center; gap: 12px;
  }
  .brand-dot {
    width: 22px; height: 22px; border-radius: 50%; background: var(--blue);
  }
  .brand-name {
    font-weight: 700; font-size: 26px; letter-spacing: .5px; color: var(--blue);
    white-space: nowrap;
  }
  .holder {
    position: absolute; left: 0; right: 0; top: 345px;
    text-align: center; font-weight: 700; font-size: 25px; color: var(--white);
  }
  .holder .first { color: var(--blue); }
  .contact-row {
    position: absolute; left: 40px; right: 40px;
    display: flex; flex-direction: column; align-items: center;
  }
  .contact-row.phone { top: 398px; }
  .contact-row.email { top: 455px; }
  .contact-rule {
    position: absolute; top: 14px; left: 0; right: 0; height: 1.5px; background: var(--blue-deep);
  }
  .contact-icon {
    position: relative; width: 30px; height: 30px; border-radius: 50%;
    background: var(--blue); border: 3px solid var(--black);
    box-shadow: 0 0 0 2px var(--blue);
    display: flex; align-items: center; justify-content: center;
  }
  .contact-text {
    margin-top: 6px; color: var(--white); font-size: 17px; font-weight: 500; letter-spacing: .5px;
  }
  .contact-row.email .contact-text { font-size: 15px; }
  .web-band {
    position: absolute; left: 0; right: 0; bottom: 0; height: 64px;
    background: var(--blue);
    border-top: 6px solid var(--white);
    display: flex; align-items: center; justify-content: center;
    color: var(--black); font-size: 16px; font-weight: 600; letter-spacing: .4px;
  }

  /* Back card */
  .card-back {
    left: 560px; top: 210px; width: 560px; height: 350px;
    background: var(--black);
  }
  .back-decoration {
    position: absolute; right: 0; top: 0; width: 250px; height: 100%;
    background: linear-gradient(160deg, #9a9a9a, var(--grey-light) 45%, var(--grey-dark));
    border-radius: 0 22px 22px 140px;
    opacity: .85;
  }
  .back-brand {
    position: absolute; left: 40px; top: 48px;
    display: flex; align-items: center; gap: 10px;
  }
  .back-brand .brand-name { font-size: 24px; }
  .back-brand .brand-dot { width: 18px; height: 18px; }
  .back-details {
    position: absolute; left: 40px; bottom: 52px;
    color: var(--white); font-size: 15px; line-height: 1.7; letter-spacing: .3px;
  }
  .back-details .trades { font-weight: 500; }
</style>
</head>
<body>
<main class="stage">

  <section class="card card-front" aria-label="Business card front">
    <div class="front-top"></div>
    <svg class="front-swoosh" viewBox="0 0 380 120" preserveAspectRatio="none" aria-hidden="true">
      <path d="M0 38 C120 20 260 40 380 110 L380 120 L0 120 Z" fill="var(--blue)"/>
      <path d="M0 48 C130 34 270 54 380 118 L380 120 L0 120 Z" fill="var(--black)"/>
      <path d="M110 46 C220 40 320 70 380 100" stroke="var(--white)" stroke-width="2" fill="none"/>
    </svg>

    <div class="brand">
      <span class="brand-dot"></span>
      <span class="brand-name">Korvane Plumbing</span>
    </div>

    <h1 class="holder"><span class="first">Dorian</span> Malvessey</h1>

    <div class="contact-row phone">
      <span class="contact-rule"></span>
      <span class="contact-icon">
        <svg width="12" height="16" viewBox="0 0 12 16" aria-hidden="true">
          <rect x="1" y="1" width="10" height="14" rx="2" fill="none" stroke="var(--black)" stroke-width="1.6"/>
          <circle cx="6" cy="12.3" r="1" fill="var(--black)"/>
        </svg>
      </span>
      <span class="contact-text">0461 590 314</span>
    </div>

    <div class="contact-row email">
      <span class="contact-rule"></span>
      <span class="contact-icon">
        <svg width="16" height="12" viewBox="0 0 16 12" aria-hidden="true">
          <rect x="1" y="1" width="14" height="10" rx="1" fill="none" stroke="var(--black)" stroke-width="1.6"/>
          <path d="M1 1 L8 7 L15 1" fill="none" stroke="var(--black)" stroke-width="1.6"/>
        </svg>
      </span>
      <span class="contact-text">info@korvaneplumbing.example</span>
    </div>

    <div class="web-band">www.korvaneplumbing.example</div>
  </section>

  <section class="card card-back" aria-label="Business card back">
    <div class="back-decoration" role="img" aria-label="Large grey pipe and tap decoration"></div>
    <div class="back-brand">
      <span class="brand-dot"></span>
      <span class="brand-name">Korvane Plumbing</span>
    </div>
    <div class="back-details">
      <p class="trades">Plumber | Drainer | Gasfitter | Roofer</p>
      <p class="ids">ABN- 42 198 603 771 | LIC- 516042D</p>
    </div>
  </section>

</main>
</body>
</html>
```